Creative, Colorful, Dynamic Infographic for Global Non-Profit

We are a global arts and education non-profit in need of an infographic that illustrates four key skills embedded in our work: Curiosity, Listening, Imagination, Postive Action.
We work primarily with educators, students, and artists who use the power of personal stories to build community and connection and to bridge divides.
Our new brand guidelines, logos, and fonts are here: https://stylekit.example/lanternfold-9
I've attached a mock-up of the graphic and the required text. (Note the attached design was created by a staff person, your final design does not need to be the same. The color scheme and text of the final design should match the brand guidelines above.)
The graphic will be used for both web and print media and should include the purple Lanternfold 9 logo (also attached).
Ideally the final design will delight audiences and spark interest in our work.

```html
<!DOCTYPE html>
<html lang="en">
<head>
<meta charset="utf-8">
<title>Lanternfold 9 — Four Skills Cycle</title>
<link rel="stylesheet" href="https://fonts.googleapis.com/css2?family=Open+Sans:wght@400;700&display=swap">
<style>
  :root {
    --bg-top: #f3f3f6;
    --bg-bottom: #e3e3eb;
    --disc: #f1f1f4;
    --disc-inner: #ebebef;
    --ring: #c8c8ce;
    --flow: #8a8a90;
    --ink: #4a4a4f;
    --teal: #9dd8cb;
    --orange: #fcc375;
    --lilac: #d3bcd8;
    --salmon: #fb907c;
    --hub-ring: #d6d7da;
    --hub-face: #f7f7f9;
    --brand: #6a2f93;
    --white: #ffffff;
  }
  html, body {
    margin: 0;
    padding: 0;
    overflow: hidden;
  }
  body {
    width: 1200px;
    height: 1200px;
    background: linear-gradient(180deg, var(--bg-top), var(--bg-bottom));
    font-family: "Open Sans", Arial, sans-serif;
  }
  .skills-cycle {
    display: block;
    width: 1200px;
    height: 1200px;
  }
  .skill-title {
    font-weight: 700;
    font-size: 12.5px;
    fill: var(--ink);
    text-decoration: underline;
    text-anchor: middle;
  }
  .skill-body {
    font-size: 11px;
    fill: var(--ink);
    text-anchor: middle;
  }
  .link-text {
    font-size: 10.5px;
    fill: var(--ink);
    text-anchor: middle;
  }
  .brand-name {
    font-size: 15px;
    font-weight: 700;
    fill: var(--white);
    text-anchor: middle;
  }
  .flow-arc {
    fill: none;
    stroke: var(--flow);
    stroke-width: 1.6;
    stroke-dasharray: 6 5;
  }
  .flow-dot { fill: var(--flow); }
  .petal { stroke: var(--disc-inner); stroke-width: 7; stroke-linejoin: round; }
  .petal-teal { fill: var(--teal); }
  .petal-orange { fill: var(--orange); }
  .petal-lilac { fill: var(--lilac); }
  .petal-salmon { fill: var(--salmon); }
  .link-circle { stroke: var(--white); stroke-width: 5; }
  .link-arrow { stroke: var(--white); stroke-width: 3; stroke-linejoin: round; }
  .icon-slot { fill: var(--ink); opacity: 0.18; }
</style>
</head>
<body>
<svg class="skills-cycle" viewBox="0 0 1024 1024" xmlns="http://www.w3.org/2000/svg" aria-label="Four skills cycle: Curiosity, Listening, Imagination, Positive action">
  <defs>
    <filter id="soft-shadow" x="-20%" y="-20%" width="140%" height="140%">
      <feDropShadow dx="0" dy="4" stdDeviation="8" flood-color="#000" flood-opacity="0.12"/>
    </filter>
    <filter id="hub-shadow" x="-40%" y="-40%" width="180%" height="180%">
      <feDropShadow dx="4" dy="8" stdDeviation="7" flood-color="#000" flood-opacity="0.25"/>
    </filter>
    <marker id="flow-head" viewBox="0 0 10 10" refX="6" refY="5" markerWidth="7" markerHeight="7" orient="auto">
      <path d="M0 1 L9 5 L0 9 Z" fill="#8a8a90"/>
    </marker>
    <path id="petal" d="M80 -282 A294 294 0 0 1 282 80 C270 86 255 92 230 95 C190 100 150 80 115 55 C60 20 30 -70 55 -115 C80 -150 100 -190 95 -230 C92 -255 86 -270 80 -282 Z"/>
  </defs>

  <!-- outer disc -->
  <circle cx="505" cy="510" r="348" fill="var(--disc)" filter="url(#soft-shadow)"/>
  <circle cx="505" cy="510" r="336" fill="none" stroke="var(--ring)" stroke-width="3"/>
  <circle cx="505" cy="510" r="326" fill="var(--disc-inner)"/>

  <!-- flow arcs -->
  <g class="flow">
    <path class="flow-arc" d="M220 619 A305 305 0 0 0 436 807" marker-end="url(#flow-head)"/>
    <circle class="flow-dot" cx="220" cy="619" r="5"/>
    <path class="flow-arc" d="M772 658 A305 305 0 0 0 810 515" marker-end="url(#flow-head)"/>
    <circle class="flow-dot" cx="772" cy="658" r="5"/>
    <path class="flow-arc" d="M774 367 A305 305 0 0 0 589 217" marker-end="url(#flow-head)"/>
    <circle class="flow-dot" cx="774" cy="367" r="5"/>
    <path class="flow-arc" d="M286 298 A305 305 0 0 0 209 436" marker-end="url(#flow-head)"/>
    <circle class="flow-dot" cx="286" cy="298" r="5"/>
  </g>

  <!-- petals -->
  <g class="petals" transform="translate(505 510)">
    <use href="#petal" class="petal petal-orange"/>
    <use href="#petal" class="petal petal-lilac" transform="rotate(90)"/>
    <use href="#petal" class="petal petal-salmon" transform="rotate(180)"/>
    <use href="#petal" class="petal petal-teal" transform="rotate(270)"/>
  </g>

  <!-- link circles with arrows -->
  <g class="links" transform="translate(505 510)">
    <g class="link link-imagination">
      <circle class="link-circle" cx="200" cy="-15" r="64" fill="var(--lilac)"/>
      <path class="link-arrow" fill="var(--lilac)" d="M168 92 L188 52 L176 50 L206 38 L212 70 L202 62 L182 100 Z"/>
    </g>
    <g class="link link-listening" transform="rotate(90)">
      <circle class="link-circle" cx="200" cy="-15" r="64" fill="var(--salmon)"/>
      <path class="link-arrow" fill="var(--salmon)" d="M168 92 L188 52 L176 50 L206 38 L212 70 L202 62 L182 100 Z"/>
    </g>
    <g class="link link-curiosity" transform="rotate(180)">
      <circle class="link-circle" cx="200" cy="-15" r="64" fill="var(--teal)"/>
      <path class="link-arrow" fill="var(--teal)" d="M168 92 L188 52 L176 50 L206 38 L212 70 L202 62 L182 100 Z"/>
    </g>
    <g class="link link-action" transform="rotate(270)">
      <circle class="link-circle" cx="200" cy="-15" r="64" fill="var(--orange)"/>
      <path class="link-arrow" fill="var(--orange)" d="M168 92 L188 52 L176 50 L206 38 L212 70 L202 62 L182 100 Z"/>
    </g>
  </g>

  <!-- hub -->
  <g class="hub">
    <circle cx="505" cy="510" r="96" fill="var(--hub-ring)"/>
    <circle cx="505" cy="510" r="74" fill="var(--hub-face)" filter="url(#hub-shadow)"/>
    <circle cx="505" cy="510" r="62" fill="var(--brand)"/>
    <text class="brand-name" x="505" y="506">Lanternfold</text>
    <text class="brand-name" x="505" y="526">9</text>
  </g>

  <!-- skill labels -->
  <g class="skill skill-curiosity">
    <text class="skill-title" x="345" y="327">Curiosity</text>
    <text class="skill-body" x="345" y="348">Focus on how you can</text>
    <text class="skill-body" x="345" y="360">learn from another’s</text>
    <text class="skill-body" x="345" y="372">knowledge and</text>
    <text class="skill-body" x="345" y="384">experience</text>
  </g>
  <g class="skill skill-action">
    <text class="skill-title" x="676" y="381">Positive action</text>
    <text class="skill-body" x="676" y="402">Show your words and</text>
    <text class="skill-body" x="676" y="414">actions matter</text>
  </g>
  <g class="skill skill-imagination">
    <text class="skill-title" x="643" y="649">Imagination</text>
    <text class="skill-body" x="643" y="670">LConsider</text>
    <text class="skill-body" x="643" y="682">possibilities</text>
    <text class="skill-body" x="643" y="694">beyond what you</text>
    <text class="skill-body" x="643" y="706">know</text>
  </g>
  <g class="skill skill-listening">
    <text class="skill-title" x="333" y="605">Listening</text>
    <text class="skill-body" x="333" y="626">Seek to understand</text>
    <text class="skill-body" x="333" y="638">before speaking</text>
  </g>

  <!-- link texts -->
  <g class="link-copy">
    <text class="link-text" x="509" y="269">Your positive</text>
    <text class="link-text" x="509" y="280">actions lead</text>
    <text class="link-text" x="509" y="291">to curiosity</text>
    <text class="link-text" x="509" y="302">about what</text>
    <text class="link-text" x="509" y="313">else is possible</text>
    <g role="img" aria-label="Icon: person with question marks"><circle class="icon-slot" cx="509" cy="333" r="11"/></g>

    <text class="link-text" x="305" y="495">Your curiosity</text>
    <text class="link-text" x="305" y="506">allows you</text>
    <text class="link-text" x="305" y="517">to listen</text>
    <g role="img" aria-label="Icon: listening ear"><circle class="icon-slot" cx="305" cy="538" r="11"/></g>

    <text class="link-text" x="505" y="677">Your listening</text>
    <text class="link-text" x="505" y="688">allows you</text>
    <text class="link-text" x="505" y="699">to take in new</text>
    <text class="link-text" x="505" y="710">information</text>
    <g role="img" aria-label="Icon: brain with lightbulb"><circle class="icon-slot" cx="505" cy="734" r="11"/></g>

    <text class="link-text" x="705" y="464">Your</text>
    <text class="link-text" x="705" y="475">imagination</text>
    <text class="link-text" x="705" y="486">can spark</text>
    <text class="link-text" x="705" y="497">positive action</text>
    <g role="img" aria-label="Icon: head with sparks of ideas"><circle class="icon-slot" cx="705" cy="520" r="12"/></g>
  </g>
</svg>
</body>
</html>
```